Handout Flyer For Medical Practice (This is Exciting!)

We need a single page handout that showcases the doctors in our medical practice and their specific specialities.

On the front I would like the pictures of the Doctors, names and their specialties. One the back, Map and Contact information for the practice

Attached in the files is what we are currently using and we do want anything that looks such as that.

Industry/Entity Type

Medical

Font styles to use
Serif

Colors
3176b5
0456a4

Requirements
Must have
• Up to date look. Would like a modern touch.

```html
<!DOCTYPE html>
<html lang="en">
<head>
<meta charset="utf-8">
<title>Riverbend Orthopedic &amp; Spine Institute – Handout</title>
<link href="https://fonts.googleapis.com/css2?family=Lato:wght@400;700&family=Roboto+Condensed:wght@400&family=Tinos:wght@700&display=swap" rel="stylesheet">
<style>
  :root{
    --blue:#0456a4;
    --blue-mid:#3176b5;
    --blue-soft:#8ea9d4;
    --blue-pale:#c9d8ee;
    --ink:#1d1d1d;
    --white:#ffffff;
    --paper:#ffffff;
    --bg:#ffffff;
  }
  *{margin:0;padding:0;box-sizing:border-box}
  html,body{width:1200px;height:812px;overflow:hidden;background:var(--bg)}
  .canvas{position:relative;width:1200px;height:812px}
  .page{position:absolute;width:494px;height:693px;background:var(--paper);overflow:hidden;
        box-shadow:3px 4px 8px rgba(0,0,0,.35)}
  .page--front{left:66px;top:64px}
  .page--back{left:633px;top:56px;height:694px}
  .page-bg{position:absolute;inset:0}

  .brand{position:absolute;font-family:"Tinos",serif;font-weight:700;line-height:1.05}
  .brand--front{left:52px;top:42px;color:var(--white);font-size:17px}
  .brand--back{left:44px;top:527px;color:var(--blue);font-size:17px}
  .brand-dot{position:absolute;width:9px;height:9px;border-radius:50%}
  .brand-dot--front{left:38px;top:46px;background:var(--white)}
  .brand-dot--back{left:30px;top:531px;background:var(--blue)}

  .divider{position:absolute;width:1px}
  .divider--front{left:287px;top:34px;height:66px;background:var(--white)}
  .divider--back{left:270px;top:498px;height:88px;background:var(--blue-mid)}

  .header-contact{position:absolute;left:301px;top:38px;color:var(--white);
        font-family:"Lato",sans-serif;font-weight:700;font-size:11px;line-height:1.32}

  .doctor{position:absolute;height:80px}
  .doctor-photo{position:absolute;left:0;top:0;width:80px;height:80px;border:3px solid var(--blue);
        border-radius:8px;background:linear-gradient(180deg,#9fb3c4 0%,#5b6f83 55%,#2c3440 100%);z-index:2}
  .doctor-label{position:absolute;left:74px;top:14px;height:50px;width:150px;background:var(--blue-soft);
        border-radius:0 12px 12px 0;padding:4px 6px 0 12px;
        font-family:"Roboto Condensed",sans-serif;font-size:11.2px;line-height:1.3;color:var(--ink)}
  .doctor-label--wide{width:160px}

  .about{position:absolute;left:26px;top:598px;width:442px;text-align:center;
        font-family:"Lato",sans-serif;font-size:8.4px;line-height:1.35;color:var(--ink)}

  .map{position:absolute;inset:0}

  .back-contact{position:absolute;left:290px;top:513px;font-family:"Lato",sans-serif;font-weight:700;
        font-size:12.5px;line-height:24px;color:var(--ink)}
  .web{position:absolute;left:0;right:0;top:670px;text-align:center;font-family:"Lato",sans-serif;
        font-weight:700;font-size:14px;letter-spacing:7px;color:var(--white)}
</style>
</head>
<body>
<div class="canvas">

  <!-- Front: team -->
  <section class="page page--front">
    <svg class="page-bg" width="494" height="693" viewBox="0 0 494 693">
      <defs>
        <radialGradient id="frontTint" cx="0.5" cy="0.5" r="0.7">
          <stop offset="0" stop-color="#ffffff"/>
          <stop offset="1" stop-color="#e9ecf1"/>
        </radialGradient>
      </defs>
      <rect width="494" height="693" fill="url(#frontTint)"/>
      <path d="M0 0H494V112C420 118 260 120 40 132Q0 136 0 170Z" fill="var(--blue)"/>
      <path d="M0 176Q0 140 40 138C250 126 420 124 494 118" fill="none" stroke="var(--blue-pale)" stroke-width="4"/>
      <path d="M0 652C160 640 330 642 460 632Q494 628 494 600V693H0Z" fill="var(--blue)"/>
      <path d="M0 646C160 634 330 636 458 626Q488 622 494 596" fill="none" stroke="var(--blue-pale)" stroke-width="4"/>
    </svg>

    <span class="brand-dot brand-dot--front"></span>
    <div class="brand brand--front">Riverbend Orthopedic<br>&amp; Spine Institute</div>
    <span class="divider divider--front"></span>
    <div class="header-contact">2450 Alder Creek Road, Ste.<br>210, Maplewood, OR 97402<br>Phone: 541-555-0142<br>www.riverbendosi.com</div>

    <div class="doctor" style="left:20px;top:186px">
      <div class="doctor-photo" role="img" aria-label="Portrait of Daniel R. Whitford, MD"></div>
      <div class="doctor-label">Daniel R. Whitford, MD<br>Physical Medicine &amp;<br>Rehabilitation specialist</div>
    </div>
    <div class="doctor" style="left:260px;top:190px">
      <div class="doctor-photo" role="img" aria-label="Portrait of Michael T. Arden, MD"></div>
      <div class="doctor-label">Michael T. Arden, MD<br>Orthopedic surgeon<br>specializing in spine</div>
    </div>
    <div class="doctor" style="left:20px;top:280px">
      <div class="doctor-photo" role="img" aria-label="Portrait of Steven J. Haldane, MD"></div>
      <div class="doctor-label" style="padding-top:10px">Steven J. Haldane, MD<br>Orthopedic surgeon</div>
    </div>
    <div class="doctor" style="left:260px;top:280px">
      <div class="doctor-photo" role="img" aria-label="Portrait of Brian K. Mercer, Jr., MD"></div>
      <div class="doctor-label doctor-label--wide">Brian K. Mercer, Jr., MD<br>Orthopedic Surgeon &amp; Sports<br>Medicine &amp; Shoulder Specialist</div>
    </div>
    <div class="doctor" style="left:20px;top:374px">
      <div class="doctor-photo" role="img" aria-label="Portrait of Laura E. Pennington, MD, MS"></div>
      <div class="doctor-label">Laura E. Pennington, MD, MS<br>Physical Medicine &amp;<br>Rehabilitation Specialist</div>
    </div>
    <div class="doctor" style="left:260px;top:374px">
      <div class="doctor-photo" role="img" aria-label="Portrait of Gregory L. Hale, MD"></div>
      <div class="doctor-label">Gregory L. Hale, MD<br>Physical Medicine &amp;<br>Rehabilitation Specialist</div>
    </div>
    <div class="doctor" style="left:150px;top:475px">
      <div class="doctor-photo" role="img" aria-label="Portrait of J. Peter Lindqvist, MD"></div>
      <div class="doctor-label" style="padding-top:10px">J. Peter Lindqvist, MD<br>Orthopedic surgeon</div>
    </div>

    <p class="about">Riverbend Orthopedic &amp; Spine Institute provides leading-edge, results-based care for orthopedic and spine disorders. We are a comprehensive, premier team of specialists dedicated to the diagnosis, treatment, rehabilitation and prevention of sports and orthopedic injuries and conditions. Our team is dedicated to improving the quality of life for our patients and their families.</p>
  </section>

  <!-- Back: location and contact -->
  <section class="page page--back">
    <svg class="page-bg" width="495" height="694" viewBox="0 0 495 694">
      <path d="M0 0H495V6Q495 36 460 40H40Q0 42 0 80Z" fill="var(--blue)"/>
      <svg class="map" x="0" y="0" width="495" height="694" role="img" aria-label="Street map showing the institute's location">
        <defs>
          <linearGradient id="mapTone" x1="0" y1="0" x2="1" y2="1">
            <stop offset="0" stop-color="#ebe7df"/>
            <stop offset="1" stop-color="#e2ded2"/>
          </linearGradient>
        </defs>
        <path d="M0 90Q0 48 44 46H495V420H60Q0 420 0 380Z" fill="url(#mapTone)"/>
      </svg>
      <path d="M0 360Q2 418 70 424C220 432 400 424 460 430Q495 436 495 470V694H0Z" fill="var(--paper)"/>
      <path d="M0 380Q0 428 60 432C220 438 400 430 458 436Q495 442 495 478" fill="none" stroke="var(--blue)" stroke-width="7"/>
      <rect x="0" y="626" width="495" height="68" fill="var(--blue)"/>
    </svg>

    <span class="brand-dot brand-dot--back"></span>
    <div class="brand brand--back">Riverbend Orthopedic<br>&amp; Spine Institute</div>
    <span class="divider divider--back"></span>
    <div class="back-contact">Tel : (541) 555-0142<br>Fax : (541) 555-0187<br>Email : info@riverbendosi.com</div>
    <div class="web">www.riverbendosi.com</div>
  </section>

</div>
</body>
</html>
```